Velquora Design
Would like the design to go over the page in a way that can type over it.
We are a personal training and small group studio
Want it to be professional and classy
Updates
Project Deadline Extended
Reason: Asked for some modifications on a few designs, want to give the designers time to do this
Target Market(s)
All age groups, sports professionals as well as business professionals, families
Industry/Entity Type
Training
Requirements
Must have
- Must have Velquora Studio
Mina Tellaver
214 Barnicot Lane
Wexcombe Vale
South Australia 5173
Phone: 0438917263
Nice to have
- Professional classy fonts
Colour
Should not have
- Clip art
Balloons

```html
<!DOCTYPE html>
<html lang="en">
<head>
<meta charset="utf-8">
<title>Velquora Studio Letterhead</title>
<link rel="stylesheet" href="https://fonts.googleapis.com/css2?family=Source+Sans+3:wght@400;600;700;800&display=swap">
<style>
  :root {
    --paper: #ffffff;
    --brand-blue: #1aa3dc;
    --deep-blue: #1b5fae;
    --accent-orange: #f07a1a;
    --ink: #222222;
    --ink-soft: #444444;
    --watermark: #efefef;
  }
  * { margin: 0; padding: 0; box-sizing: border-box; }
  html, body {
    width: 934px; height: 1200px; overflow: hidden;
    background: var(--paper);
    font-family: "Source Sans 3", "Myriad Pro", Arial, sans-serif;
  }
  .letterhead { position: relative; width: 934px; height: 1200px; background: var(--paper); }

  .rule { position: absolute; height: 3px; background: var(--accent-orange); top: 123px; }
  .rule--left { left: 0; width: 62px; }
  .rule--main { left: 340px; width: 447px; }
  .rule--edge { left: 895px; width: 39px; }

  .brand-mark {
    position: absolute; left: 62px; top: 72px;
    display: flex; align-items: center; gap: 12px;
  }
  .brand-mark__dot {
    width: 26px; height: 26px; border-radius: 50%;
    border: 5px solid var(--accent-orange);
  }
  .brand-mark__name {
    font-weight: 800; font-size: 38px; line-height: 1;
    color: var(--deep-blue); letter-spacing: -0.5px;
  }

  .contact {
    position: absolute; right: 146px; top: 26px;
    text-align: right; font-size: 14px; line-height: 1.25; color: var(--ink-soft);
  }
  .contact__studio { color: var(--brand-blue); font-weight: 700; font-size: 16px; margin-right: -6px; }
  .contact__person { color: var(--ink); font-weight: 700; font-size: 14.5px; margin-bottom: 6px; }
  .contact__label { color: var(--brand-blue); font-weight: 700; }
  .contact__line { margin-right: 6px; }
  .contact__line--email { margin-right: 6px; }

  .address {
    position: absolute; right: 147px; top: 142px;
    text-align: right; font-size: 14px; line-height: 1.25; color: var(--ink-soft);
  }

  .watermark {
    position: absolute; left: 0; width: 934px; top: 610px;
    display: flex; flex-direction: column; align-items: center; gap: 26px;
  }
  .watermark__dot {
    width: 110px; height: 110px; border-radius: 50%;
    border: 22px solid var(--watermark);
  }
  .watermark__name {
    font-weight: 800; font-size: 96px; line-height: 1; color: var(--watermark);
  }
</style>
</head>
<body>
  <main class="letterhead">
    <div class="rule rule--left"></div>
    <div class="rule rule--main"></div>
    <div class="rule rule--edge"></div>

    <div class="brand-mark">
      <span class="brand-mark__dot"></span>
      <span class="brand-mark__name">Velquora Studio</span>
    </div>

    <section class="contact">
      <p class="contact__studio">Velquora Studio</p>
      <p class="contact__person">Mina Tellaver</p>
      <p class="contact__line"><span class="contact__label">Phone</span> : 0438917263</p>
      <p class="contact__line--email"><span class="contact__label">Email</span> : info@velquora.com</p>
    </section>

    <address class="address" style="font-style: normal;">
      <p>214 Barnicot Lane</p>
      <p>Wexcombe Vale</p>
      <p>South Australia 5173</p>
    </address>

    <div class="watermark" aria-hidden="true">
      <span class="watermark__dot"></span>
      <span class="watermark__name">Velquora</span>
    </div>
  </main>
</body>
</html>
```